Spices producer needs product label design.

I need a two label design of 90mm(H) x 60mm(H) for multiple line of spices and other product. First label for the front should have the logo, and second label should be the same as the first but without the logo. I would like the same dark reddish colour on my logo for the design if possible or similar. This label will be use for multiple products, so a clear in-between space is important to add information and change product name for printing . I would prefer a mixture of traditional and rustic style.
I have attached my logos and sample on how I would like the look.

Target Market(s)

25-60 women and men.

Industry/Entity Type

Retail

Requirements
Must have
• As stated above.
Nice to have
• Please see attached sample .
Should not have
• Multiple colours, animation design.

```html
<!DOCTYPE html>
<html lang="en">
<head>
<meta charset="utf-8">
<title>TAZORI Spice Labels – Front and Back</title>
<link rel="stylesheet" href="https://fonts.googleapis.com/css2?family=Alegreya:ital,wght@0,800;1,700&family=Roboto+Condensed:wght@400&display=swap">
<style>
  :root {
    --wine: #7a1518;
    --wine-deep: #6c1212;
    --wine-soft: #84241e;
    --cream: #f5e9d2;
    --ink: #111111;
    --paper: #ffffff;
  }
  * { box-sizing: border-box; margin: 0; padding: 0; }
  html, body {
    width: 1200px;
    height: 785px;
    overflow: hidden;
    background: var(--paper);
  }
  .sheet {
    position: relative;
    width: 1200px;
    height: 785px;
  }

  /* dimension marks */
  .dim-h, .dim-v { position: absolute; }
  .dim-h {
    top: 82px;
    width: 357px;
    height: 28px;
    border-left: 1px solid var(--ink);
    border-right: 1px solid var(--ink);
  }
  .dim-h::after {
    content: "";
    position: absolute;
    left: 0; right: 0; top: 18px;
    border-top: 1px solid var(--ink);
  }
  .dim-v {
    top: 127px;
    width: 29px;
    height: 535px;
    border-top: 1px solid var(--ink);
    border-bottom: 1px solid var(--ink);
  }
  .dim-v::after {
    content: "";
    position: absolute;
    top: 0; bottom: 0; left: 14px;
    border-left: 1px solid var(--ink);
  }
  .dim-label {
    position: absolute;
    font-family: "Roboto Condensed", sans-serif;
    font-size: 22px;
    color: var(--ink);
    padding: 0 4px;
    line-height: 1;
    white-space: nowrap;
  }
  .dim-h .dim-label {
    left: 50%;
    top: -9px;
    transform: translateX(-50%);
  }
  .dim-v .dim-label {
    left: -16px;
    top: 50%;
    transform: translate(-50%, -50%) rotate(-90deg);
  }

  /* label */
  .label {
    position: absolute;
    top: 127px;
    width: 357px;
    height: 535px;
    overflow: hidden;
  }
  .label-pattern {
    position: absolute;
    inset: 0;
    background:
      radial-gradient(circle at 20% 30%, var(--wine-soft) 0%, transparent 40%),
      radial-gradient(circle at 85% 70%, var(--wine-soft) 0%, transparent 40%),
      linear-gradient(180deg, var(--wine) 0%, var(--wine-deep) 100%);
  }
  .label-panel {
    position: absolute;
    left: 50px;
    top: 0;
    width: 257px;
    height: 510px;
  }
  .brand-name {
    position: absolute;
    left: 70px;
    top: 40px;
    width: 217px;
    text-align: center;
    font-family: "Alegreya", serif;
    font-weight: 800;
    font-size: 50px;
    line-height: 1;
    letter-spacing: 1px;
    color: var(--wine);
    white-space: nowrap;
  }
  .tagline-band {
    position: absolute;
    left: 77px;
    top: 116px;
    width: 202px;
    height: 29px;
    background: var(--wine);
    display: flex;
    align-items: center;
    justify-content: center;
  }
  .tagline {
    font-family: "Alegreya", serif;
    font-style: italic;
    font-weight: 700;
    font-size: 24px;
    color: var(--cream);
    line-height: 1;
    white-space: nowrap;
  }
</style>
</head>
<body>
<main class="sheet">

  <!-- front label -->
  <div class="dim-h" style="left:195px;"><span class="dim-label">60 mm.</span></div>
  <div class="dim-v" style="left:141px;"><span class="dim-label">90 mm.</span></div>

  <section class="label label--front" style="left:195px;" aria-label="Front label">
    <div class="label-pattern" role="img" aria-label="Dark wine-red border with traditional floral swirl pattern"></div>
    <svg class="label-panel" viewBox="0 0 257 510" aria-hidden="true">
      <path fill="var(--cream)" d="M0 0 H257 V508
        c-4 0 -6 -10 -12.85 -10 c-6.85 0 -8.85 10 -12.85 10
        c-4 0 -6 -10 -12.85 -10 c-6.85 0 -8.85 10 -12.85 10
        c-4 0 -6 -10 -12.85 -10 c-6.85 0 -8.85 10 -12.85 10
        c-4 0 -6 -10 -12.85 -10 c-6.85 0 -8.85 10 -12.85 10
        c-4 0 -6 -10 -12.85 -10 c-6.85 0 -8.85 10 -12.85 10
        c-4 0 -6 -10 -12.85 -10 c-6.85 0 -8.85 10 -12.85 10
        c-4 0 -6 -10 -12.85 -10 c-6.85 0 -8.85 10 -12.85 10
        c-4 0 -6 -10 -12.85 -10 c-6.85 0 -8.85 10 -12.85 10
        c-4 0 -6 -10 -12.85 -10 c-6.85 0 -8.85 10 -12.85 10
        c-4 0 -6 -10 -12.85 -10 c-6.85 0 -8.85 10 -12.85 10 Z"/>
      <line x1="8" y1="0" x2="8" y2="492" stroke="var(--wine)" stroke-width="1.5"/>
      <line x1="249" y1="0" x2="249" y2="492" stroke="var(--wine)" stroke-width="1.5"/>
    </svg>
    <h1 class="brand-name">TAZORI</h1>
    <div class="tagline-band"><p class="tagline">Artisan quality</p></div>
  </section>

  <!-- back label -->
  <div class="dim-h" style="left:681px;"><span class="dim-label">60 mm.</span></div>
  <div class="dim-v" style="left:628px;"><span class="dim-label">90 mm.</span></div>

  <section class="label label--back" style="left:681px;" aria-label="Back label">
    <div class="label-pattern" role="img" aria-label="Dark wine-red border with traditional floral swirl pattern"></div>
    <svg class="label-panel" viewBox="0 0 257 510" aria-hidden="true">
      <path fill="var(--cream)" d="M0 0 H257 V508
        c-4 0 -6 -10 -12.85 -10 c-6.85 0 -8.85 10 -12.85 10
        c-4 0 -6 -10 -12.85 -10 c-6.85 0 -8.85 10 -12.85 10
        c-4 0 -6 -10 -12.85 -10 c-6.85 0 -8.85 10 -12.85 10
        c-4 0 -6 -10 -12.85 -10 c-6.85 0 -8.85 10 -12.85 10
        c-4 0 -6 -10 -12.85 -10 c-6.85 0 -8.85 10 -12.85 10
        c-4 0 -6 -10 -12.85 -10 c-6.85 0 -8.85 10 -12.85 10
        c-4 0 -6 -10 -12.85 -10 c-6.85 0 -8.85 10 -12.85 10
        c-4 0 -6 -10 -12.85 -10 c-6.85 0 -8.85 10 -12.85 10
        c-4 0 -6 -10 -12.85 -10 c-6.85 0 -8.85 10 -12.85 10
        c-4 0 -6 -10 -12.85 -10 c-6.85 0 -8.85 10 -12.85 10 Z"/>
      <line x1="8" y1="0" x2="8" y2="492" stroke="var(--wine)" stroke-width="1.5"/>
      <line x1="249" y1="0" x2="249" y2="492" stroke="var(--wine)" stroke-width="1.5"/>
    </svg>
  </section>

</main>
</body>
</html>
```